marketing card

I need a fun and striking Marketing card to introduce our new office to attract new patients
our website is smilepathwaykids@mailbrook.net for more ideas
add coupon for $25.00 off your next filling
add coupon for free teeth whitening
make the card 9x6 size ,
The card downloaded I like rediscover your smile
free teeth whitening after exam,x-rays & cleaning
Target Market(s)
population in our area , anyone looking for a dental office
Industry/Entity Type
Health Care
Font styles to use
Serif
Colors
33a6d7
9bcb3c
Requirements
Must have
- Coupon for $25 off if you need a filling
- free whitening after teeth cleaning, x-rays & exam
- Our hygienist will come to you if you are home bound or in a nursing home facility
Nice to have
- want to be inviting and non intimating, we see all ages

```html
<!DOCTYPE html>
<html lang="en">
<head>
<meta charset="utf-8">
<title>Bright Path Smiles – Marketing Card</title>
<link rel="stylesheet" href="https://fonts.googleapis.com/css2?family=Oswald:wght@500;700&family=Roboto:wght@300;400;700&display=swap">
<style>
  :root {
    --page-bg: #ebe7e1;
    --brand-green: #5c9a25;
    --line-green: #6fae38;
    --navy: #153e66;
    --steel: #6f8fa8;
    --sky: #a9c1d6;
    --ink: #1f2a3a;
    --logo-grey: #e4e6ea;
    --logo-ink: #3a4f8a;
    --white: #ffffff;
  }
  * { box-sizing: border-box; margin: 0; padding: 0; }
  html, body { width: 1200px; height: 1200px; overflow: hidden; background: var(--page-bg); }
  body { position: relative; font-family: "Roboto", Arial, sans-serif; }

  .card {
    position: absolute;
    left: 195px;
    width: 864px;
    height: 576px;
    transform: scale(0.9375);
    transform-origin: top left;
    background: var(--white);
    overflow: hidden;
    box-shadow: 0 14px 24px rgba(0,0,0,0.18);
  }
  .card--front { top: 40px; }
  .card--back { top: 620px; }
  .card__art { position: absolute; inset: 0; width: 100%; height: 100%; }

  .brand-strip {
    position: absolute;
    display: flex;
    height: 32px;
    width: 344px;
  }
  .brand-strip__name {
    width: 100px;
    background: var(--logo-grey);
    display: flex;
    align-items: center;
    justify-content: center;
    gap: 5px;
    font-weight: 700;
    font-size: 10.5px;
    color: var(--logo-ink);
    white-space: nowrap;
  }
  .brand-strip__mark { width: 7px; height: 7px; background: var(--logo-ink); }
  .brand-strip__tagline {
    flex: 1;
    background: var(--brand-green);
    color: #1d2b12;
    font-size: 7.6px;
    line-height: 10px;
    padding: 6px 8px 6px 12px;
    white-space: nowrap;
    clip-path: polygon(8px 0, 100% 0, 100% 100%, 0 100%);
  }
  .card--front .brand-strip { left: 25px; top: 32px; }
  .card--back .brand-strip { left: 490px; top: 508px; }

  .offer { position: absolute; left: 26px; display: flex; align-items: flex-end; gap: 10px; color: var(--white); }
  .offer__tag {
    font-family: "Oswald", Impact, sans-serif;
    font-weight: 700;
    font-size: 34px;
    line-height: 42px;
    padding: 0 18px 0 4px;
  }
  .offer__text { font-weight: 300; font-size: 22px; line-height: 30px; }
  .offer--filling { top: 120px; }
  .offer--filling .offer__tag { background: var(--brand-green); clip-path: polygon(0 0, 100% 0, 88% 100%, 0 100%); }
  .offer--whitening { top: 181px; }
  .offer--whitening .offer__tag { background: var(--white); color: var(--brand-green); clip-path: polygon(0 0, 100% 0, 93% 100%, 0 100%); }
  .offer__more { position: absolute; left: 30px; top: 224px; color: var(--white); font-weight: 300; font-size: 22px; }

  .home-visit { position: absolute; left: 30px; top: 268px; color: var(--ink); font-size: 14px; line-height: 18px; font-weight: 300; }

  .business-name {
    position: absolute;
    right: 32px;
    top: 192px;
    font-family: "Oswald", Impact, sans-serif;
    font-weight: 700;
    font-size: 42px;
    line-height: 58px;
    color: var(--brand-green);
    white-space: nowrap;
  }
  .contact {
    position: absolute;
    right: 32px;
    top: 260px;
    text-align: right;
    font-style: normal;
    font-size: 14px;
    line-height: 17.6px;
    font-weight: 300;
    color: var(--ink);
  }
  .mission {
    position: absolute;
    right: 32px;
    top: 440px;
    text-align: right;
    font-size: 13.5px;
    line-height: 18px;
    font-weight: 300;
    color: var(--ink);
    white-space: nowrap;
  }
</style>
</head>
<body>

<section class="card card--front">
  <svg class="card__art" viewBox="0 0 864 576" preserveAspectRatio="none">
    <defs>
      <linearGradient id="greenery" x1="0" y1="0" x2="1" y2="1">
        <stop offset="0" stop-color="#2f7a3a"/>
        <stop offset="0.45" stop-color="#6fae5a"/>
        <stop offset="1" stop-color="#cfe3cf"/>
      </linearGradient>
      <linearGradient id="family" x1="0" y1="0" x2="1" y2="1">
        <stop offset="0" stop-color="#eef3ee"/>
        <stop offset="0.5" stop-color="#d9c9bd"/>
        <stop offset="1" stop-color="#9fb7c4"/>
      </linearGradient>
    </defs>
    <rect class="photo-greenery" width="864" height="576" fill="url(#greenery)" role="img" aria-label="Blurred green trees in sunlight"/>
    <path class="field-white" d="M200 576 C320 480 430 320 520 200 C600 100 680 30 752 0 L864 0 L864 576 Z" fill="#ffffff"/>
    <path class="photo-family" d="M864 78 C700 93 540 228 430 338 C340 430 260 520 190 576 L864 576 Z" fill="url(#family)" role="img" aria-label="Smiling family of four outdoors, parents carrying children piggyback"/>
    <path class="line-green" d="M864 78 C700 93 540 228 430 338 C340 430 260 520 190 576" fill="none" stroke="var(--line-green)" stroke-width="3"/>
    <path class="corner-white" d="M0 478 C100 500 220 470 330 400 C250 480 180 540 130 576 L0 576 Z" fill="#ffffff"/>
    <path class="corner-line" d="M0 478 C100 500 220 470 330 400" fill="none" stroke="var(--line-green)" stroke-width="5"/>
    <path class="band-steel" d="M192 576 C300 490 400 330 476 215 C532 130 570 45 600 0 L752 0 C680 30 600 100 520 200 C430 320 320 480 200 576 Z" fill="var(--steel)"/>
    <path class="band-navy" d="M112 576 C250 500 380 320 460 200 C520 110 560 40 586 0 L600 0 C570 45 532 130 476 215 C400 330 300 490 192 576 Z" fill="var(--navy)"/>
  </svg>

  <div class="brand-strip">
    <div class="brand-strip__name"><span class="brand-strip__mark"></span>Bright Path</div>
    <div class="brand-strip__tagline">We are here for what's best for you, not what best for us!<br>YOU deserve Excellent Dental Care.</div>
  </div>

  <div class="offer offer--filling"><span class="offer__tag">$25 OFF</span><span class="offer__text">for filling</span></div>
  <div class="offer offer--whitening"><span class="offer__tag">FREE WHITENING</span><span class="offer__text">after teeth</span></div>
  <p class="offer__more">cleaning, x- ray &amp; exam</p>

  <p class="home-visit">Our hygienist will come to you<br>if you are home bound or<br>in a nursing home facility.</p>
</section>

<section class="card card--back">
  <svg class="card__art" viewBox="0 0 864 576" preserveAspectRatio="none">
    <defs>
      <linearGradient id="greenery-back" x1="0" y1="0" x2="1" y2="1">
        <stop offset="0" stop-color="#3f8a3c"/>
        <stop offset="0.6" stop-color="#78b466"/>
        <stop offset="1" stop-color="#d6e8d2"/>
      </linearGradient>
      <linearGradient id="band-fade" x1="0" y1="0" x2="0" y2="1">
        <stop offset="0" stop-color="#6f8fa8"/>
        <stop offset="1" stop-color="#a9c1d6"/>
      </linearGradient>
    </defs>
    <path class="photo-greenery" d="M0 0 L386 0 C350 110 310 190 272 255 C200 310 100 350 0 360 Z" fill="url(#greenery-back)" role="img" aria-label="Blurred green trees in sunlight"/>
    <path class="corner-line" d="M0 360 C100 350 200 310 272 255" fill="none" stroke="var(--line-green)" stroke-width="4"/>
    <path class="line-green" d="M557 0 C470 70 380 150 300 235" fill="none" stroke="var(--line-green)" stroke-width="2"/>
    <path class="band-sky" d="M0 497 C190 445 320 250 400 0 L442 0 C350 260 210 470 0 525 Z" fill="url(#band-fade)"/>
    <path class="band-navy" d="M0 470 C180 420 300 240 380 0 L400 0 C320 250 190 445 0 497 Z" fill="var(--navy)"/>
  </svg>

  <h1 class="business-name">BRIGHT PATH SMILES</h1>
  <address class="contact">
    Email: youremail@email.com<br>
    Call us: 012-555-555<br>
    Address: location4321 Any street,<br>
    your city, country 4351<br>
    www.yourwebsite.com
  </address>
  <p class="mission">Your mission: ed ut perspiciatis, unde omnis iste natus error sit<br>voluptatem accusantium doloremque laudantium, totam rem aperiam<br>eaque ipsa, quae ab</p>

  <div class="brand-strip">
    <div class="brand-strip__name"><span class="brand-strip__mark"></span>Bright Path</div>
    <div class="brand-strip__tagline">We are here for what's best for you, not what best for us!<br>YOU deserve Excellent Dental Care.</div>
  </div>
</section>

</body>
</html>
```